Site for a workout and Consulting enterprise

I need a professional responsive site for www.olvaru.hamburg. The website shoulderstand consist of a Landing and 4 other pages. - On page for the contact informations - on page for the about - on page for consulting services (technical) - on page for Training and workshop services (business and soft skills) I add some files so you can see my idea of the design.
Target Market(s)
IT and Management
Industry/Entity Type
Management Consulting
Coding
Coded - Design and coding required
Number of Pages Required
4 page
Requirements
Must have
- Use Pictures for Background, Sliders and Topics. Just have to placeholders for the design.

```html
<!DOCTYPE html>
<html lang="de">
<head>
<meta charset="utf-8">
<title>Olvaru – Individuen, Ideen, Innovationen</title>
<link href="https://fonts.googleapis.com/css2?family=Montserrat:wght@500;700&family=Arimo:wght@400&display=swap" rel="stylesheet">
<style>
  :root {
    --panel: #9cb5c4;
    --hero-light: #b7cdd8;
    --hero-mid: #8fa8b8;
    --hero-dark: #5e7a90;
    --navy: #2b4f6c;
    --accent-blue: #2d5676;
    --muted-grey: #7b7f83;
    --white: #ffffff;
    --icon-ring: #5d6e7a;
    --icon-fill: #c3d3dc;
    --orange: #f0932b;
  }
  * { margin: 0; padding: 0; box-sizing: border-box; }
  html, body { width: 1200px; height: 675px; overflow: hidden; background: var(--panel); }
  .page { position: relative; width: 1200px; height: 675px; overflow: hidden; background: var(--panel); }

  .hero-visual {
    position: absolute; left: 0; top: 0; width: 600px; height: 675px;
    background:
      radial-gradient(circle at 30% 45%, rgba(255,255,255,0.35), transparent 45%),
      radial-gradient(circle at 85% 30%, rgba(255,255,255,0.25), transparent 30%),
      linear-gradient(100deg, var(--hero-light) 0%, var(--hero-mid) 55%, var(--hero-dark) 100%);
  }

  .brand { position: absolute; left: 72px; top: 262px; }
  .brand-name {
    font-family: "Montserrat", sans-serif; font-weight: 700;
    font-size: 132px; line-height: 1; color: var(--navy); letter-spacing: -2px;
  }
  .brand-tagline {
    position: absolute; left: 77px; top: 398px;
    font-family: "Arimo", sans-serif; font-size: 31px; color: var(--white);
  }

  .menu-toggle { position: absolute; left: 576px; top: 326px; width: 48px; height: 48px; }

  .services { position: absolute; left: 668px; top: 260px; list-style: none; }
  .service { display: flex; align-items: center; height: 60px; margin-bottom: 45px; }
  .service-icon { width: 59px; height: 59px; flex: none; }
  .service-label {
    margin-left: 17px; font-family: "Montserrat", sans-serif; font-weight: 700;
    font-size: 22px; letter-spacing: 0.3px;
  }
  .service--consulting .service-label { color: var(--accent-blue); }
  .service--workshops .service-label { color: var(--muted-grey); }

  .footer-links {
    position: absolute; left: 785px; top: 614px;
    font-family: "Montserrat", sans-serif; font-weight: 500; font-size: 23px;
    color: var(--accent-blue);
  }
</style>
</head>
<body>
<main class="page">
  <div class="hero-visual" role="img" aria-label="Photo of a businessman in a suit touching glowing interface gears"></div>

  <div class="brand">
    <div class="brand-name">Olvaru</div>
  </div>
  <p class="brand-tagline">Individuen, Ideen, Innovationen</p>

  <svg class="menu-toggle" viewBox="0 0 48 48" aria-label="Menü öffnen">
    <circle cx="24" cy="24" r="24" fill="var(--navy)"/>
    <rect x="11" y="20.5" width="26" height="7" fill="var(--white)"/>
    <rect x="20.5" y="11" width="7" height="26" fill="var(--white)"/>
  </svg>

  <ul class="services">
    <li class="service service--consulting">
      <svg class="service-icon" viewBox="0 0 60 60" role="img" aria-label="Icon of a light bulb with a gear">
        <circle cx="30" cy="30" r="28.5" fill="var(--icon-fill)" stroke="var(--icon-ring)" stroke-width="1.5"/>
        <circle cx="30" cy="28" r="8" fill="none" stroke="var(--orange)" stroke-width="3"/>
        <rect x="26" y="38" width="8" height="6" fill="var(--icon-ring)"/>
      </svg>
      <span class="service-label">CONSULTING</span>
    </li>
    <li class="service service--workshops">
      <svg class="service-icon" viewBox="0 0 60 60" role="img" aria-label="Icon of a head with a gear">
        <circle cx="30" cy="30" r="28.5" fill="var(--icon-fill)" stroke="var(--icon-ring)" stroke-width="1.5"/>
        <circle cx="30" cy="27" r="12" fill="var(--white)" stroke="var(--icon-ring)" stroke-width="1.5"/>
        <circle cx="30" cy="25" r="4" fill="none" stroke="var(--icon-ring)" stroke-width="2"/>
      </svg>
      <span class="service-label">WORKSHOPS</span>
    </li>
  </ul>

  <nav class="footer-links">Impressum | Contact</nav>
</main>
</body>
</html>
```